Quillory homepage (design only)

We need a high-impact design (alone) for the homepage for a new service to be launched shortly.

Quillory.com will allow consumers to generate a free 'financial personality' report which will help people protect themselves from being mis-sold inappropriate products and services by the financial services industry.

We have upload the Quillory logo and associated artwork. You have totally free reign to use these as you see fit, including using different colours to the lime green we've used.

We ONLY want a design and would prefer it in Illustrator CS5 or lower format rather than Photoshop bitmap. We will write any necessary code or CSS for the final page.

We intend the end site to utilise html5 type animation and effects extensively so if you are picturing an animation, please ensure you explain it with your submission.

The homepage will have five main elements:

1. Navigation:
- Why Quillory
- Security
- Sample report
- Do the test

2. Main section - Quillory : Know Your Financial Personality (you can add ipsum lorum 'explanatory text' if you see fit). This section should refer to the services output, a report which shows five financial characteristics:
- Personality type
- Investment approach
- Knowledge
- Decision biases
- % of UK population like you

3. 'See how you compare against the UK'. An important output of the report is the fact it is linked to extensive UK research. When a user has completed the test, Quillory show him or her via an info graphic, whist percentage of the UK population shares their attributes. Accompnaying tex reads: " If you've ever wondered how you compare to others when it comes to your attitudes on money related matters, quillory will show you". There is an attached file called 'infographic' that illustrates what the end infogrpahic might look like. You can choose to refer to this or elements of this in this section if you choose.

4. 'Cut out the stuff not relevant to you' Accompanying text could be: "Whether it’s language, unnecessarily complex products or stuff that may be too plain risky for you, your Quillory report will help filter out all of the stuff that’s less relevant to you leaving you with choices you understand and decisions that are easier to make." we imagine this section leading to a page that will explain the complexity of products and services before a Quillory report and the small number of relevant services after a quillory report. This section should illustrate that before and after concept.

5. 'Take the test' This section is critical, its the 'call to action' element of the page that links straight to the test. It should illustrate that the test is very short, and very easy.. only two very interactive steps before you get results:
1. Click on the graphics that best describe you.
2. Drag some questions into Quillory 'answer buckets'
3. Done! See the results.
4. Give your free profile to any online service (we make it simple)

The emphasis here is on illustration, typography, colour and impact. We want the site to feel consumer and accessible, not too stuffy and financial, at the same time not too childlike. We are not in favour of typical 'financial' library pics, we'd prefer illustration. Please use your own creativity

Target Market(s)

Adults typically aged 30+ with majority in 40's - 60's. People considering investing or taking any kind of financial advice,

Industry/Entity Type

Financial

Font styles to use
Sans Serif

Requirements
Must have
• The design must include the attached quillory logo albeit the colours used can be entirely at your discretion.
Nice to have
• Site designs we like include:
http://www.fennelvault.example

Should not have
• Design should not contain 'bamboo' clip art. If any quillory type artwork is needed, if should be a derivative of the attached 'bamboo stalk' file. Ideally no stock photography. Illustration and typography should dominate.

Should not use serif fonts

```html
<!DOCTYPE html>
<html lang="en">
<head>
<meta charset="utf-8">
<title>Quillory – Know Your Financial Personality</title>
<link rel="stylesheet" href="https://fonts.googleapis.com/css2?family=Arimo:wght@400;700&family=Questrial&display=swap">
<style>
:root{
  --lime:#7dc24b;
  --lime-soft:#85c54f;
  --lime-pale:#c9e6b0;
  --stalk:#d6ebc2;
  --stalk-deep:#c3e1a6;
  --leaf-dark:#4a7d2a;
  --forest:#5e923a;
  --mist:#f1f7ea;
  --ink:#1e1e1e;
  --grey:#8a8a8a;
  --grey-line:#d9d9d9;
  --track:#666666;
  --orange:#f47a3c;
  --male:#3aa3e0;
  --female:#e7a1d8;
  --white:#ffffff;
}
*{margin:0;padding:0;box-sizing:border-box}
html,body{width:1200px;height:2372px;overflow:hidden;background:var(--white)}
body{font-family:"Arimo",Arial,sans-serif;color:var(--ink);position:relative}
.page{position:relative;width:1200px;height:2372px;overflow:hidden}
.abs{position:absolute}

/* header */
.topbar{left:0;top:0;width:1200px;height:88px;background:linear-gradient(#d4ebc0,#a9d585);z-index:2}
.brand-disc{left:122px;top:8px;width:130px;height:130px;border-radius:50%;background:var(--lime);border:5px solid var(--white);box-shadow:0 2px 6px rgba(0,0,0,.25);z-index:5}
.brand-name{left:268px;top:40px;font-size:34px;line-height:38px;color:var(--ink);letter-spacing:1px;z-index:3}
.main-nav{left:0;top:57px;width:1200px;font-size:16px;line-height:18px;color:var(--ink);z-index:3}
.main-nav span{position:absolute;white-space:nowrap}

/* hero */
.hero{left:0;top:88px;width:1200px;height:451px;background:linear-gradient(#ffffff 0%,var(--mist) 100%)}
.hero-art{left:600px;top:88px;width:500px;height:451px;background:linear-gradient(100deg,rgba(214,235,194,0) 0%,var(--stalk) 35%,var(--stalk-deep) 60%,rgba(214,235,194,0) 100%)}
.hero-title{left:180px;top:186px;font-family:"Arimo",Arial,sans-serif;font-weight:400;font-size:70px;line-height:76px;color:var(--lime)}
.hero-tagline{left:193px;top:266px;font-size:21px;line-height:24px;color:var(--leaf-dark)}
.traits{left:312px;top:314px;list-style:none}
.traits li{position:relative;height:36px;padding-left:20px;font-size:18px;line-height:28px}
.traits li::before{content:"";position:absolute;left:0;top:1px;width:10px;height:26px;background:var(--lime)}

/* compare */
.compare-title{left:0;top:578px;width:1074px;text-align:center;font-size:28px;line-height:34px;font-weight:400;color:var(--leaf-dark)}
.compare-quote{left:407px;top:626px;width:530px;font-size:15.5px;line-height:20px;color:var(--leaf-dark)}
.rule{left:0;width:1200px;height:3px;background:var(--grey-line)}
.infographic{left:0;top:720px}

/* filter band */
.band-edge{left:0;top:1164px;width:1200px;height:20px;background:var(--lime-pale)}
.band{left:0;top:1184px;width:1200px;height:412px;background:var(--lime-soft)}
.band-title{left:179px;top:1308px;font-size:34px;line-height:38px;font-weight:400;color:var(--white)}
.band-quote{left:203px;top:1390px;width:820px;font-size:19px;line-height:26px;color:var(--white)}

/* call to action */
.cta-button{left:493px;top:1693px;width:218px;height:52px;background:var(--lime);color:var(--white);font-size:24px;font-weight:700;text-align:center;line-height:52px;box-shadow:0 2px 4px rgba(0,0,0,.2)}
.steps{left:380px;top:1772px;font-size:15px;line-height:19px;list-style:none}

/* footer */
.footer{left:0;top:1947px;width:1200px;height:425px;background:var(--forest)}
.footer-text{color:var(--white)}
.footer-brand{left:162px;top:2057px;font-size:34px;line-height:38px}
.footer-disc{left:216px;top:2112px;width:75px;height:75px;border-radius:50%;background:var(--lime);border:3px solid var(--white)}
.footer-col{border-left:1px solid rgba(255,255,255,.7);font-size:15px;padding-left:8px}
.footer-col span{display:block;white-space:nowrap}
.col-site{left:380px;top:2027px;height:120px;line-height:33px}
.col-support{left:572px;top:2056px;height:190px;line-height:27px}
.support-title{left:471px;top:2184px;font-size:22px;line-height:26px;font-weight:700}
.touch-title{left:745px;top:2030px;font-size:14px;line-height:18px;font-weight:700}
.social-divider{left:860px;top:2027px;width:1px;height:155px;background:rgba(255,255,255,.7)}
.social{left:876px;width:32px;height:32px;background:#111}
.legal{left:0;top:2326px;width:1200px;font-size:11px;line-height:14px}
.legal span{position:absolute;white-space:nowrap}
</style>
</head>
<body>
<div class="page">

  <header>
    <div class="abs topbar"></div>
    <div class="abs brand-disc"></div>
    <div class="abs brand-name">Quillory</div>
    <nav class="abs main-nav">
      <span style="left:505px">Why &nbsp;Quillory</span>
      <span style="left:668px">Security</span>
      <span style="left:773px">Sample report</span>
      <span style="left:916px">Do the test</span>
    </nav>
  </header>

  <section>
    <div class="abs hero"></div>
    <div class="abs hero-art" role="img" aria-label="Pale green stalk and leaf artwork behind the hero"></div>
    <h1 class="abs hero-title">Quillory</h1>
    <p class="abs hero-tagline">Know Your Financial Personality</p>
    <ul class="abs traits">
      <li>Personality type</li>
      <li>Investment approach</li>
      <li>Knowledge</li>
      <li>Decision biases</li>
      <li>% of UK population like you</li>
    </ul>
  </section>

  <section>
    <h2 class="abs compare-title">See how you compare against the UK</h2>
    <p class="abs compare-quote">"If you've ever wondered how you compare to others when it comes to your attitudes on money related matters, quillory will show you"</p>
    <div class="abs rule" style="top:709px"></div>
    <svg class="abs infographic" width="1200" height="420" viewBox="0 720 1200 420" font-family="Arimo, Arial, sans-serif">
      <path d="M248 788 V925 Q248 935 258 935 H500 Q510 935 510 945 V1080 Q510 1090 520 1090 H955 Q965 1090 965 1080 V1015" fill="none" stroke="var(--track)" stroke-width="6"/>
      <circle cx="248" cy="770" r="25" fill="#fff" stroke="var(--track)" stroke-width="6"/>
      <circle cx="965" cy="990" r="25" fill="#fff" stroke="var(--track)" stroke-width="6"/>
      <text x="280" y="774" font-size="13" fill="var(--grey)">Tomas</text>
      <circle cx="286" cy="865" r="11" fill="var(--orange)"/><text x="286" y="869" font-size="9" fill="#fff" text-anchor="middle">47%</text>
      <g fill="var(--male)"><circle cx="290" cy="891" r="4"/><rect x="285" y="897" width="10" height="20" rx="2"/></g>
      <g fill="var(--female)"><circle cx="314" cy="891" r="4"/><path d="M308 913 L314 897 L320 913Z"/></g>
      <text x="265" y="960" font-size="12" fill="var(--grey)">Gender</text>
      <text x="346" y="960" font-size="12" fill="var(--grey)">Age</text>
      <circle cx="290" cy="935" r="3" fill="var(--orange)"/><circle cx="356" cy="935" r="3" fill="var(--orange)"/>
      <g font-size="9" fill="var(--grey)">
        <rect x="345" y="830" width="14" height="8" fill="#999"/><text x="368" y="838">30's – 16%</text>
        <rect x="345" y="856" width="14" height="8" fill="#222"/><text x="368" y="864" fill="#222">40's</text>
        <circle cx="402" cy="861" r="11" fill="var(--orange)"/><text x="402" y="865" fill="#fff" text-anchor="middle">52%</text>
        <rect x="345" y="882" width="14" height="8" fill="#999"/><text x="368" y="890">50's – 28%</text>
        <rect x="345" y="908" width="14" height="8" fill="#999"/><text x="368" y="916">60's – 15%</text>
      </g>
      <g font-size="11" fill="#fff" text-anchor="middle">
        <circle cx="584" cy="855" r="18" fill="#bdbdbd"/><text x="584" y="859">17%</text>
        <circle cx="584" cy="915" r="24" fill="var(--orange)"/><text x="584" y="919" font-weight="700">28%</text>
        <circle cx="584" cy="974" r="22" fill="#bdbdbd"/><text x="584" y="978">27%</text>
        <circle cx="584" cy="1040" r="22" fill="#bdbdbd"/><text x="584" y="1044">28%</text>
        <circle cx="758" cy="808" r="20" fill="#dedede"/><text x="758" y="812">10%</text>
        <circle cx="758" cy="860" r="18" fill="#fff" stroke="#eee"/><text x="758" y="864" fill="var(--orange)" font-weight="700">16%</text>
        <circle cx="758" cy="922" r="24" fill="#c8c8c8"/><text x="758" y="926">23%</text>
        <circle cx="758" cy="986" r="24" fill="#d0d0d0"/><text x="758" y="990">25%</text>
        <circle cx="758" cy="1050" r="20" fill="#dedede"/><text x="758" y="1054">10%</text>
      </g>
      <circle cx="584" cy="1090" r="3" fill="var(--orange)"/><circle cx="758" cy="1090" r="3" fill="var(--orange)"/>
      <text x="584" y="1112" font-size="12" fill="var(--grey)" text-anchor="middle">Financial Knowledge</text>
      <text x="764" y="1112" font-size="12" fill="var(--grey)" text-anchor="middle">Risk aptitude</text>
      <text x="930" y="886" font-size="12" fill="var(--grey)">% like me</text>
      <g>
        <g fill="var(--male)"><rect x="944" y="894" width="6" height="10"/><rect x="954" y="894" width="6" height="10"/><rect x="964" y="894" width="6" height="10"/><rect x="974" y="894" width="6" height="10"/><rect x="984" y="894" width="6" height="10"/></g>
        <g fill="#bbb"><rect x="944" y="910" width="6" height="10"/><rect x="954" y="910" width="6" height="10"/><rect x="964" y="910" width="6" height="10"/><rect x="974" y="910" width="6" height="10"/><rect x="984" y="910" width="6" height="10"/>
        <rect x="944" y="926" width="6" height="10"/><rect x="954" y="926" width="6" height="10"/><rect x="964" y="926" width="6" height="10"/><rect x="974" y="926" width="6" height="10"/><rect x="984" y="926" width="6" height="10"/>
        <rect x="944" y="942" width="6" height="10"/><rect x="954" y="942" width="6" height="10"/><rect x="964" y="942" width="6" height="10"/><rect x="974" y="942" width="6" height="10"/><rect x="984" y="942" width="6" height="10"/></g>
      </g>
    </svg>
  </section>

  <section>
    <div class="abs band-edge"></div>
    <div class="abs band"></div>
    <h2 class="abs band-title">Cut out the stuff not relevant to you</h2>
    <p class="abs band-quote">"Whether it's language, unnecessarily complex products or stuff that may be too plain risky for you, your Quillory report will help filter out all of the stuff that's less relevant to you leaving you with choices you understand and decisions that are easier to make."</p>
    <div class="abs rule" style="top:1653px"></div>
  </section>

  <section>
    <div class="abs cta-button">TAKE THE TEST</div>
    <ol class="abs steps">
      <li>1. Click on the graphics that best describe you.</li>
      <li>2. Drag some questions into Quillory 'answer buckets'</li>
      <li>3. Done! See the results.</li>
      <li>4. Give your free profile to any online service (we make it simple)</li>
    </ol>
    <div class="abs rule" style="top:1925px;height:2px;background:#eeeeee"></div>
  </section>

  <footer>
    <div class="abs footer"></div>
    <div class="abs footer-text footer-brand">Quillory</div>
    <div class="abs footer-disc"></div>
    <div class="abs footer-text footer-col col-site">
      <span>Why &nbsp;Quillory</span><span>Security</span><span>Sample report</span><span>Do the test</span>
    </div>
    <div class="abs footer-text support-title">Support</div>
    <div class="abs footer-text footer-col col-support">
      <span>home</span><span>FAQs</span><span>Sitemap</span><span>hello@quillory.com</span><span>005550155</span><span>Office</span><span>020 0005512</span>
    </div>
    <div class="abs footer-text touch-title">Keep in touch</div>
    <div class="abs social-divider"></div>
    <div class="abs social" style="top:2030px"></div>
    <div class="abs social" style="top:2066px"></div>
    <div class="abs social" style="top:2102px"></div>
    <div class="abs social" style="top:2138px"></div>
    <div class="abs footer-text legal">
      <span style="left:226px">Privacy policy</span>
      <span style="left:342px">Site terms</span>
      <span style="left:459px">Terms and conditions</span>
      <span style="left:620px">Regulatory</span>
      <span style="left:743px;font-weight:700">© 2014 Quillory Limited</span>
    </div>
  </footer>

</div>
</body>
</html>
```